New Album "A night beside the silver hills"

I need a cd cover for a new pop rock album called "A night beside the silver hills"
The main color of the artwork shall obviously be orange. The artwork shouldn't be too "obvious", but it would be better something a bit abstract.
Please remember that it is a Music Cd Cover, so do not send business logo or advertisement images.

Target Market(s)

It's a pop rock album, so the target customers are young and adult people from 15-60 years old

Requirements
Must have
• Orange as main colour
The Artist name is: Remy Castellan
The Title: A night beside the silver hills
Should not have
• Not too cheesy or dreamy images please. No simple sunset or sunrise pics

```html
<!DOCTYPE html>
<html lang="en">
<head>
<meta charset="utf-8">
<title>A Night Beside the Silver Hills — Remy Castellan</title>
<link rel="stylesheet" href="https://fonts.googleapis.com/css2?family=Josefin+Sans:wght@400;600&family=Montserrat:wght@600&display=swap">
<style>
  :root {
    --sky-top: #f4e88a;
    --sky-mid: #f4cf7e;
    --sky-bottom: #ebb072;
    --cloud-light: #f8e196;
    --cloud-mid: #f1c77f;
    --cloud-edge: rgba(240, 190, 120, 0);
    --floor-shadow: rgba(196, 140, 90, 0.55);
    --type: #ffffff;
  }
  html, body {
    margin: 0;
    padding: 0;
    width: 1200px;
    height: 1200px;
    overflow: hidden;
  }
  .album-cover {
    position: relative;
    width: 1200px;
    height: 1200px;
    overflow: hidden;
    background: linear-gradient(180deg, var(--sky-top) 0%, var(--sky-mid) 50%, var(--sky-bottom) 100%);
  }
  .cover-cloud {
    position: absolute;
    left: 390px;
    top: 415px;
    width: 480px;
    height: 330px;
    border-radius: 50% 48% 45% 50% / 55% 50% 45% 45%;
    background: radial-gradient(ellipse at 45% 40%, var(--cloud-light) 0%, var(--cloud-mid) 55%, var(--cloud-edge) 75%);
    filter: blur(6px);
  }
  .floor-shadow {
    position: absolute;
    left: 430px;
    top: 948px;
    width: 380px;
    height: 34px;
    border-radius: 50%;
    background: radial-gradient(ellipse at center, var(--floor-shadow) 0%, rgba(196, 140, 90, 0) 70%);
    filter: blur(4px);
  }
  .album-title {
    position: absolute;
    left: 0;
    right: 0;
    top: 582px;
    margin: 0;
    text-align: center;
    font-family: "Josefin Sans", sans-serif;
    font-weight: 600;
    font-size: 28px;
    letter-spacing: 0.45em;
    text-indent: 0.45em;
    line-height: 1;
    color: var(--type);
    text-transform: uppercase;
  }
  .artist-name {
    position: absolute;
    left: 0;
    right: 0;
    top: 1008px;
    margin: 0;
    text-align: center;
    font-family: "Montserrat", sans-serif;
    font-weight: 600;
    font-size: 23px;
    letter-spacing: 0.45em;
    text-indent: 0.45em;
    line-height: 1;
    color: var(--type);
    text-transform: uppercase;
  }
</style>
</head>
<body>
  <main class="album-cover">
    <div class="cover-cloud" role="img" aria-label="A soft, glowing pale orange cloud floating in the centre of the cover"></div>
    <div class="floor-shadow"></div>
    <h1 class="album-title">A night beside the silver hills</h1>
    <p class="artist-name">Remy Castellan</p>
  </main>
</body>
</html>
```